The Brightwater Compass Business Card

We need an attractive business card with the logo that we bought from ArtVantly last year.
Our mission is to contribute to change the way today's leaders manage business companies bringing value to the workplace and helping them to build a new model of creating wealth.
Our logo is clear about our values : we seek Positive Change through People and are convinced that the pursuit of individual well-being and the chase of economic results can converge with the right management.
Management Consulting
Corinne Fabrelle
+34 612 98 70 31
corinne.fabrelle@thebrightwatercompass-mail.net
www.thebrightwatercompass-mail.net

```html
<!DOCTYPE html>
<html lang="en">
<head>
<meta charset="utf-8">
<title>The Brightwater Compass – Business Card</title>
<link rel="stylesheet" href="https://fonts.googleapis.com/css2?family=Cinzel:wght@400;600&family=Roboto:wght@400&display=swap">
<style>
  :root {
    --teal: #11827e;
    --teal-dark: #0e6f6b;
    --white: #ffffff;
    --ink: #5a5f63;
    --backdrop: #2b2c2e;
  }
  * { margin: 0; padding: 0; box-sizing: border-box; }
  html, body { width: 1200px; height: 900px; overflow: hidden; }
  body { background: var(--backdrop); position: relative; font-family: "Roboto", Arial, sans-serif; }

  .card { position: absolute; width: 640px; height: 366px; box-shadow: 0 10px 28px rgba(0,0,0,.45); }

  /* Front */
  .card-front { left: 80px; top: 70px; background: var(--teal); display: flex; flex-direction: column; align-items: center; justify-content: center; gap: 22px; }
  .brand-mark { width: 46px; height: 46px; border-radius: 50%; background: var(--white); }
  .brand-name { font-family: "Cinzel", "Times New Roman", serif; font-weight: 600; color: var(--white); font-size: 38px; letter-spacing: 2px; text-align: center; line-height: 1.2; }

  /* Back */
  .card-back { left: 480px; top: 470px; background: var(--white); }
  .back-brand { position: absolute; right: 44px; top: 44px; display: flex; align-items: center; gap: 12px; }
  .back-brand .brand-mark { width: 28px; height: 28px; background: var(--teal); }
  .back-brand .brand-name { color: var(--teal); font-size: 20px; letter-spacing: 1px; }

  .divider { position: absolute; left: 250px; right: 0; top: 150px; height: 3px; background: var(--teal); }

  .contacts { position: absolute; right: 30px; top: 166px; list-style: none; text-align: right; }
  .contacts li { display: flex; justify-content: flex-end; align-items: center; gap: 10px; font-size: 13.5px; color: var(--ink); height: 24px; }
  .contacts svg { width: 14px; height: 14px; fill: var(--teal); flex: none; }
  .contacts .web strong { color: var(--teal); font-weight: 400; }

  .holder { position: absolute; left: 0; top: 250px; padding-left: 24px; border-left: 5px solid var(--teal); }
  .holder-name { font-family: "Cinzel", "Times New Roman", serif; font-weight: 400; color: var(--teal); font-size: 22px; letter-spacing: 1px; }
  .holder-role { font-size: 14px; color: var(--ink); margin-top: 2px; }
</style>
</head>
<body>
  <section class="card card-front">
    <span class="brand-mark"></span>
    <h1 class="brand-name">The Brightwater<br>Compass</h1>
  </section>

  <section class="card card-back">
    <div class="back-brand">
      <span class="brand-mark"></span>
      <span class="brand-name">The Brightwater Compass</span>
    </div>

    <div class="divider"></div>

    <ul class="contacts">
      <li>+34 612 98 70 31
        <svg viewBox="0 0 24 24"><path d="M6.6 10.8a15 15 0 0 0 6.6 6.6l2.2-2.2c.3-.3.7-.4 1-.2 1.1.4 2.3.6 3.6.6.6 0 1 .4 1 1V20c0 .6-.4 1-1 1A17 17 0 0 1 3 4c0-.6.4-1 1-1h3.5c.6 0 1 .4 1 1 0 1.3.2 2.5.6 3.6.1.3 0 .7-.2 1z"/></svg>
      </li>
      <li>corinne.fabrelle@thebrightwatercompass-mail.net
        <svg viewBox="0 0 24 24"><path d="M2 5h20v14H2z" fill="none" stroke="#11827e" stroke-width="2"/><path d="M2 5l10 8 10-8" fill="none" stroke="#11827e" stroke-width="2"/></svg>
      </li>
      <li class="web">www.<strong>thebrightwatercompass-mail</strong>.net
        <svg viewBox="0 0 24 24"><circle cx="12" cy="12" r="9" fill="none" stroke="#11827e" stroke-width="2"/><path d="M3 12h18M12 3c3 3 3 15 0 18M12 3c-3 3-3 15 0 18" fill="none" stroke="#11827e" stroke-width="1.6"/></svg>
      </li>
    </ul>

    <div class="holder">
      <h2 class="holder-name">Corinne Fabrelle</h2>
      <p class="holder-role">Managing Director</p>
    </div>
  </section>
</body>
</html>
```